Locksmith Business Cards

My father-in-law is in need of new business cards for his locksmith business and I need to impress him. Kindly help me out!

You can see the previous business card attached. It is a family run business in North Wales.

No individual names on the cards.

Key Things to Feature:
- The words "Prompt", "Local", "Reliable" (as you can see under the logo on the website)
- 24h Emergency Service
- Covering All of North Wales, the Wirral and Chester
- The color blue
- A key or a lock would be interesting (similar to the ones that come up when you google locksmith business card)

Optional (only if design includes bullet points, like the example below):
https://imgvaultcdnx.net/design_img/318264/57190/57190_2749031_318264_image.jpg
- Residential / Commercial / Automotive
- Alarms & Cameras
- Key Cutting & Safes

https://www.bryncoed-locksmiths-demo.co.uk/

Locksmith

01632 960 418
07700 900 362
bryncoedlocksmiths@mailvalex.com
Bryncoed Locksmiths, Hafod Barn, 4 Pennant Rd., Llandudno LL39 7QZ
www.bryncoed-locksmiths-demo.co.uk

• - The words "Prompt", "Local", "Reliable" (as you can see under the logo on the website)
• - 24h Emergency Service
• - Covering All of North Wales, the Wirral and Chester
• - A key or a lock would be interesting (similar to the ones that come up when you google locksmith business card)

```html
<!DOCTYPE html>
<html lang="en">
<head>
<meta charset="utf-8">
<title>Bryncoed Locksmiths – Business Cards</title>
<link rel="stylesheet" href="https://fonts.googleapis.com/css2?family=Lato:ital,wght@0,300;0,900;1,300;1,400;1,700&family=Roboto+Condensed:ital,wght@1,300&display=swap">
<style>
  :root {
    --backdrop: #2b2b2d;
    --card: #f7f7f8;
    --navy: #1e2a66;
    --ink: #4656a0;
    --shadow: rgba(0,0,0,.45);
  }
  html, body {
    margin: 0;
    width: 1200px;
    height: 960px;
    overflow: hidden;
    background: var(--backdrop);
  }
  .canvas { position: relative; width: 1200px; height: 960px; }
  .card {
    position: absolute;
    width: 586px;
    height: 334px;
    background: var(--card);
    box-shadow: 0 8px 18px var(--shadow);
    overflow: hidden;
  }
  .card--front { left: 309px; top: 119px; }
  .card--back  { left: 306px; top: 506px; }

  .key-band { position: absolute; right: 0; top: 0; width: 78px; height: 334px; }

  .brand { position: absolute; display: flex; align-items: center; }
  .brand__mark { background: var(--navy); border-radius: 10px; flex: none; }
  .brand__name {
    font-family: "Lato", sans-serif;
    font-weight: 900;
    color: var(--navy);
    text-transform: uppercase;
    letter-spacing: -0.5px;
    line-height: 0.98;
  }

  .card--front .brand { left: 72px; top: 40px; }
  .card--front .brand__mark { width: 52px; height: 72px; margin-right: 8px; }
  .card--front .brand__name { font-size: 25px; }

  .contact {
    position: absolute;
    left: 61px;
    margin: 0;
    font-family: "Roboto Condensed", sans-serif;
    font-style: italic;
    font-weight: 300;
    color: var(--ink);
    font-size: 17.5px;
    line-height: 22px;
  }
  .contact--lines { top: 125px; }
  .contact--address { top: 205px; line-height: 25px; }

  .emergency {
    position: absolute;
    left: 203px;
    top: 275px;
    margin: 0;
    font-family: "Lato", sans-serif;
    font-style: italic;
    font-weight: 700;
    font-size: 25px;
    color: var(--ink);
  }

  .card--back .brand { left: 75px; top: 82px; }
  .card--back .brand__mark { width: 96px; height: 134px; border-radius: 18px; margin-right: 12px; }
  .card--back .brand__name { font-size: 47px; }
  .tagline {
    position: absolute;
    left: 180px;
    top: 193px;
    margin: 0;
    font-family: "Lato", sans-serif;
    font-style: italic;
    font-weight: 300;
    font-size: 17px;
    letter-spacing: 2.6px;
    color: var(--ink);
  }
  .website {
    position: absolute;
    left: 0;
    right: 78px;
    top: 289px;
    margin: 0;
    text-align: center;
    font-family: "Lato", sans-serif;
    font-style: italic;
    font-weight: 400;
    font-size: 15.5px;
    color: var(--ink);
  }
</style>
</head>
<body>
<main class="canvas">

  <section class="card card--front" aria-label="Business card front">
    <div class="brand">
      <span class="brand__mark" aria-hidden="true"></span>
      <span class="brand__name">Bryncoed<br>Locksmiths</span>
    </div>
    <p class="contact contact--lines">07700 900 362<br>01632 960 418<br>bryncoedlocksmiths@mailvalex.com</p>
    <p class="contact contact--address">Bryncoed Locksmiths, Hafod Barn 4,<br>Pennant Rd., Llandudno LL39 7QZ</p>
    <p class="emergency">24h Emergency Service</p>
    <svg class="key-band" viewBox="0 0 78 334" role="img" aria-label="Dark blue key blade silhouette running down the card edge">
      <polygon points="78,0 78,334 0,334 0,295 22,270 22,40 40,22 60,22" fill="var(--navy)"/>
    </svg>
  </section>

  <section class="card card--back" aria-label="Business card back">
    <div class="brand">
      <span class="brand__mark" aria-hidden="true"></span>
      <span class="brand__name">Bryncoed<br>Locksmiths</span>
    </div>
    <p class="tagline">Prompt. Local. Reliable</p>
    <p class="website">www.bryncoed-locksmiths-demo.co.uk</p>
    <svg class="key-band" viewBox="0 0 78 334" role="img" aria-label="Dark blue key blade silhouette running down the card edge">
      <polygon points="78,0 78,334 0,334 0,295 22,270 22,40 40,22 60,22" fill="var(--navy)"/>
    </svg>
  </section>

</main>
</body>
</html>
```